Church Christmas Flyer

The flyer is to advertise our Christmas Eve services. The flyer is for a Christian church service to celebrate the birth of Jesus. We would like to see designs that use blue, silver and gold for colors but feel free to be creative. We are interested in a flyer that is has texture, depth and is more abstract than literal. Don't be afraid to layer. Please make the flyer double sided

* I uploaded our Christmas flyer from last year.

Target Market(s)

30-55 year old, male and female

Industry/Entity Type

Church

Requirements
Must have
• Map to the church
Church phone number 555-314-7096
Service times 3:00pm and 5:00pm
church address 28315 Marigold Ave, Hesperia, Ca. 92345
church website www.brookstonefellowship.example
Scripture verse

Text must stand out and be easy to read
Nice to have
• Use of the star in the sky that guided the wise men to Jesus.
Should not have
• Santa Clause, Snowmen, Reindeer

```html
<!DOCTYPE html>
<html lang="en">
<head>
<meta charset="utf-8">
<title>Christmas Eve – Brookstone Fellowship</title>
<link rel="stylesheet" href="https://fonts.googleapis.com/css2?family=Tinos:ital,wght@0,400;0,700;1,400&family=PT+Sans:wght@400;700&family=Arimo:wght@700&display=swap">
<style>
  :root {
    --page: #ffffff;
    --night: #1f4fb8;
    --night-deep: #163c94;
    --night-light: #4f86e0;
    --glow: rgba(190, 215, 255, 0.55);
    --gold: #f4c21c;
    --gold-soft: #f7d64a;
    --silver-hi: #f4f6f8;
    --silver-mid: #9aa3ad;
    --silver-lo: #5b6470;
    --white: #ffffff;
    --map-land: #e9e4d6;
    --map-road: #cfc7b2;
  }
  * { box-sizing: border-box; margin: 0; padding: 0; }
  html, body {
    width: 1200px; height: 900px; overflow: hidden;
    background: var(--page);
  }
  .canvas { position: relative; width: 1200px; height: 900px; }

  .flyer-side {
    position: absolute; left: 116px; width: 984px; height: 420px; overflow: hidden;
    background:
      radial-gradient(circle at 12% 70%, var(--glow) 0, transparent 6%),
      radial-gradient(circle at 28% 40%, rgba(255,255,255,.18) 0, transparent 9%),
      radial-gradient(circle at 46% 82%, rgba(255,255,255,.16) 0, transparent 7%),
      radial-gradient(circle at 66% 30%, rgba(255,255,255,.14) 0, transparent 8%),
      radial-gradient(circle at 84% 72%, rgba(255,255,255,.2) 0, transparent 7%),
      radial-gradient(circle at 93% 20%, rgba(255,255,255,.18) 0, transparent 6%),
      radial-gradient(ellipse at 50% 50%, var(--night-light) 0, var(--night) 55%, var(--night-deep) 100%);
  }
  .flyer-front { top: 16px; }
  .flyer-back {
    top: 460px;
    background:
      radial-gradient(ellipse at 6% 20%, rgba(220,235,255,.85) 0, rgba(140,180,240,.45) 14%, transparent 32%),
      radial-gradient(circle at 20% 65%, rgba(255,255,255,.2) 0, transparent 7%),
      radial-gradient(circle at 34% 90%, rgba(255,255,255,.16) 0, transparent 6%),
      radial-gradient(circle at 62% 12%, rgba(255,255,255,.16) 0, transparent 6%),
      radial-gradient(circle at 80% 88%, rgba(255,255,255,.14) 0, transparent 7%),
      radial-gradient(ellipse at 50% 50%, var(--night-light) 0, var(--night) 55%, var(--night-deep) 100%);
  }

  .metal-title {
    position: absolute;
    font-family: "Tinos", "Times New Roman", serif;
    font-weight: 400; letter-spacing: 2px; line-height: 1;
    background: linear-gradient(180deg, var(--silver-hi) 0%, var(--silver-mid) 45%, var(--silver-lo) 55%, var(--silver-hi) 100%);
    -webkit-background-clip: text; background-clip: text; color: transparent;
    filter: drop-shadow(2px 3px 2px rgba(0,0,0,.45));
  }

  .church-name {
    position: absolute; left: 24px; top: 12px;
    font-family: "PT Sans", Arial, sans-serif; font-weight: 700; font-size: 17px; color: var(--white);
  }
  .front-title { left: 34px; top: 42px; font-size: 88px; }
  .tagline {
    position: absolute; left: 214px; top: 124px;
    font-family: "PT Sans", Arial, sans-serif; font-size: 42px; color: var(--gold);
    letter-spacing: 1px;
    text-shadow: 0 0 14px rgba(255,220,120,.6);
  }
  .guiding-star { position: absolute; left: 874px; top: 40px; width: 80px; height: 80px; }

  .scripture {
    position: absolute; left: 0; right: 0; top: 212px; text-align: center;
    font-family: "Tinos", "Times New Roman", serif; font-style: italic;
    font-size: 36px; line-height: 50px; color: var(--white);
    text-shadow: 1px 2px 3px rgba(0,0,0,.35);
  }
  .scripture .accent { color: var(--gold); font-style: normal; font-size: 44px; }
  .scripture .accent-small { color: var(--gold); font-style: normal; }
  .reference {
    position: absolute; right: 64px; top: 380px;
    font-family: "Tinos", "Times New Roman", serif; font-size: 28px; color: var(--white);
  }

  .back-title { left: 84px; top: 12px; font-size: 80px; }
  .side-name {
    position: absolute; left: 6px; top: 16px; writing-mode: vertical-rl;
    font-family: "PT Sans", Arial, sans-serif; font-weight: 700; font-size: 27px; color: var(--gold);
  }
  .side-tagline {
    position: absolute; left: 918px; top: 20px; writing-mode: vertical-rl;
    font-family: "PT Sans", Arial, sans-serif; font-size: 17px; color: var(--gold); letter-spacing: 1px;
  }
  .side-web {
    position: absolute; left: 946px; top: 20px; writing-mode: vertical-rl;
    font-family: "PT Sans", Arial, sans-serif; font-weight: 700; font-size: 17px; color: var(--white);
  }

  .service-label {
    position: absolute; left: 108px; top: 90px;
    font-family: "PT Sans", Arial, sans-serif; font-weight: 700; font-size: 26px; color: var(--gold);
  }
  .service-date {
    position: absolute; left: 218px; top: 116px;
    font-family: "Arimo", Arial, sans-serif; font-weight: 700; font-size: 34px; color: var(--white);
    text-shadow: 1px 2px 3px rgba(0,0,0,.35);
  }
  .service-times {
    position: absolute; left: 218px; top: 156px;
    font-family: "PT Sans", Arial, sans-serif; font-weight: 700; font-size: 20px; color: var(--gold);
  }

  .map-area {
    position: absolute; left: 624px; top: 106px; width: 200px; height: 196px;
    background: linear-gradient(135deg, var(--map-land), var(--map-road));
    border: 2px solid var(--white);
  }
  .contact {
    position: absolute; left: 628px; top: 326px;
    font-family: "PT Sans", Arial, sans-serif; font-size: 20px; line-height: 28px; color: var(--white);
  }
  .contact .phone { color: var(--gold); font-weight: 700; padding-left: 30px; }
</style>
</head>
<body>
<main class="canvas">

  <section class="flyer-side flyer-front">
    <p class="church-name">Brookstone Fellowship</p>
    <h1 class="metal-title front-title">CHRISTMAS EVE</h1>
    <p class="tagline">A CELEBRATION OF GOD’S LOVE</p>
    <svg class="guiding-star" viewBox="0 0 80 80" aria-hidden="true">
      <defs>
        <radialGradient id="star-glow">
          <stop offset="0" stop-color="#fff6c8" stop-opacity=".9"/>
          <stop offset="1" stop-color="#fff6c8" stop-opacity="0"/>
        </radialGradient>
      </defs>
      <circle cx="40" cy="40" r="30" fill="url(#star-glow)"/>
      <path d="M40 2 L43 37 L78 40 L43 43 L40 78 L37 43 L2 40 L37 37 Z" fill="#fff3b0"/>
    </svg>
    <blockquote class="scripture">
      “This is how <span class="accent">GOD</span> showed his love among us<br>
      he sent his <span class="accent-small">ONE</span> and only <span class="accent">SON</span> into the world<br>
      that we might live through him.”
    </blockquote>
    <p class="reference">John 4:9</p>
  </section>

  <section class="flyer-side flyer-back">
    <p class="side-name">Brookstone Fellowship</p>
    <h2 class="metal-title back-title">CHRISTMAS EVE</h2>
    <p class="service-label">CHRISTMAS EVE SERVICE</p>
    <p class="service-date">DECEMBER 24TH</p>
    <p class="service-times">3:00 PM &amp; 5:00 PM</p>
    <div class="map-area" role="img" aria-label="Street map showing the location of the church"></div>
    <address class="contact" style="font-style:normal">
      Brookstone Fellowship<br>
      28315 Marigold Ave, Hesperia<br>
      <span class="phone">555-314-7096</span>
    </address>
    <p class="side-tagline">A CELEBRATION OF GOD’S LOVE</p>
    <p class="side-web">www.brookstonefellowship.example</p>
  </section>

</main>
</body>
</html>
```